Corwith Lodge website redesign

After 8 years of our current site, we're ready to upgrade our site design. We'd like to generally make it more modern and clean and build it on a CMS like joomla for easier future maintenance.

Our hotel is a family-owned bed and breakfast that competes against much larger hotel chains in Aspen with fancier rooms and larger pricetags. Our hotel is priced moderately and features tasteful, uniquely-design rooms.

We are looking for a website that will showcase the uniqueness of our rooms, the history of the Lodge, and the friendliness of our staff.

Here are some other hotel sites we like:

http://www.brackenfoldhouse.example/

http://www.tollerpeakhaus.example/

http://www.quarrowstay.example/

*********

Scope of Work - I'm looking for a design AND build. The website should be built out in Joomla as part of the final deliverable.
Updates

Current website: http://www.corwithlodge.example/

Explanation of what design + build means:

I am looking for not only the design of the site, but also for the homepage and one subpage to be built out as well. I do NOT need the entire site built - only for those two pages to be built and I will retrofit the remainder of the pages.

Target Market(s)

travellers evaluating hotels in Aspen, Colorado.

Industry/Entity Type

Hotel

Requirements
Must have
• Must, must, must be based on a joomla template. "Rotating" large main image as central position on homepage is a must (see example websites mentioned above).

Nice to have
• We have an existing online reservation system. It would be nice to evaluate placing a "widget" on the homepage that integrates to the online reservation page. Similar to that feature that the Bracken Fold website has at the foot of the main image on their homepage.

```html
<!DOCTYPE html>
<html lang="en">
<head>
<meta charset="utf-8">
<title>Corwith Lodge</title>
<link href="https://fonts.googleapis.com/css2?family=Source+Sans+3:wght@300;400;600&family=Ubuntu:wght@400&display=swap" rel="stylesheet">
<style>
:root{
  --bg:#000;
  --purple:#4b3f80;
  --purple-dark:#3a2f6a;
  --nav-top:#4a4a50;
  --nav-bottom:#2a2a2e;
  --text-light:#e8e8e8;
  --text-grey:#7a7a7a;
  --logo:#d8d8d8;
  --footer-link:#3d3a6b;
  --arrow:#2a6fd6;
}
*{margin:0;padding:0;box-sizing:border-box}
html,body{width:1200px;height:1024px;overflow:hidden;background:var(--bg)}
body{font-family:"Source Sans 3",Arial,sans-serif;position:relative}
.header{position:absolute;left:0;top:0;width:1200px;height:160px;
  background:radial-gradient(ellipse 420px 200px at 640px 40px,rgba(110,80,190,.55),rgba(40,25,80,.25) 60%,transparent 100%),#000}
.logo{position:absolute;left:132px;top:58px;font-size:42px;font-weight:300;color:var(--logo);letter-spacing:.5px}
.call{position:absolute;right:125px;top:62px;color:#b8b8c0;font-size:18px;font-weight:300}
.call strong{font-size:24px;font-weight:600;color:#d0d0d6;margin-left:4px}
.nav{position:absolute;left:109px;top:163px;width:980px;height:40px;border-radius:4px;
  background:linear-gradient(var(--nav-top),var(--nav-bottom));display:flex;align-items:center;padding-left:20px}
.nav a{color:#fff;text-decoration:none;font-size:13.5px;margin-right:46px}
.hero{position:absolute;left:110px;top:219px;width:980px;height:443px;border-radius:4px;overflow:hidden;
  background:linear-gradient(100deg,#3a2412 0%,#8a5a2e 25%,#c89a5c 45%,#7f8a4a 52%,#c4a070 62%,#a8764a 80%,#6b4a32 100%)}
.caption{position:absolute;left:0;top:136px;width:380px;height:98px;background:rgba(30,25,20,.7);
  color:#fff;font-size:25px;font-weight:300;line-height:34px;padding:14px 28px}
.booking{position:absolute;left:667px;top:124px;width:313px;height:319px;background:rgba(235,230,225,.5)}
.labels{position:absolute;top:7px;left:14px;font-size:10.5px;color:#222;text-transform:uppercase}
.labels span{position:absolute;white-space:nowrap}
.field{position:absolute;top:27px;height:18px;background:#fff;border:1px solid #999;font-size:9.5px;color:#b22;padding:2px 3px}
.field.sel{color:#333}
.field .ico{position:absolute;right:2px;top:2px;width:13px;height:12px;background:repeating-linear-gradient(90deg,#999 0 3px,#fff 3px 4px)}
.field .dd{position:absolute;right:1px;top:1px;width:14px;height:14px;background:#ddd;border:1px solid #666}
.book{position:absolute;left:178px;top:67px;width:119px;height:44px;background:var(--purple-dark);border-radius:3px;
  color:#fff;font-size:17px;font-weight:600;text-align:center;line-height:44px}
.menu{position:absolute;left:24px;top:63px;list-style:none}
.menu li{height:47px}
.menu b{display:block;margin-left:9px;font-size:17px;font-weight:400;color:#111;line-height:20px}
.menu small{display:block;font-size:10px;color:#333;margin-top:6px;letter-spacing:.3px}
.thumbs{position:absolute;left:133px;top:686px;display:flex;gap:2px}
.thumb{width:114px;height:76px}
.arrow{position:absolute;top:716px}
.welcome{position:absolute;left:126px;top:816px;width:962px}
.welcome h1{font-family:"Ubuntu",sans-serif;font-weight:400;font-size:22px;color:var(--purple);display:flex;align-items:center}
.welcome h1::before{content:"";width:11px;height:11px;background:var(--purple);margin-right:10px}
.welcome p{margin-top:10px;font-size:13px;line-height:18px;color:var(--text-grey);font-weight:300}
.footer{position:absolute;left:0;top:972px;width:1200px;height:52px;background:#fff;text-align:center;font-size:12.5px;color:var(--footer-link);padding-top:11px}
.footer a{color:var(--footer-link);text-decoration:none;margin:0 6px}
.footer p{margin-top:3px}
</style>
</head>
<body>
<header class="header">
  <div class="logo">Corwith Lodge</div>
  <div class="call">Book online or call <strong>877-555-0148</strong></div>
</header>
<nav class="nav">
  <a href="#">Home</a><a href="#">About</a><a href="#">Rooms</a><a href="#">Reservations</a><a href="#">Amenities</a><a href="#">Aspen information</a><a href="#">Manager's Journal</a><a href="#">Webcams</a><a href="#">Contact Us</a>
</nav>
<section class="hero" role="img" aria-label="Warm-lit guest room with armchairs, coffee table and French doors onto greenery">
  <div class="caption">We take care of everything to fullfill your every need</div>
  <div class="booking">
    <div class="labels"><span style="left:0">Arrival</span><span style="left:87px">Departure</span><span style="left:174px">Adults</span><span style="left:234px">Children</span></div>
    <div class="field" style="left:12px;width:80px">CHECK IN<i class="ico"></i></div>
    <div class="field" style="left:99px;width:80px">CHECK OUT<i class="ico"></i></div>
    <div class="field sel" style="left:185px;width:53px">--<i class="dd"></i></div>
    <div class="field sel" style="left:246px;width:54px">--<i class="dd"></i></div>
    <div class="book">BOOK NOW</div>
    <ul class="menu">
      <li><b>HOME</b><small>welcome to home</small></li>
      <li><b>RESORT</b><small>book resort</small></li>
      <li><b>BREAKFAST</b><small>order to breakfast</small></li>
      <li><b>PHOTOS</b><small>view our photos</small></li>
      <li><b>CONTACT</b><small>contact us</small></li>
    </ul>
  </div>
</section>
<svg class="arrow" style="left:109px" width="14" height="22" viewBox="0 0 14 22"><path d="M11 2 3 11l8 9" fill="none" stroke="var(--arrow)" stroke-width="3"/></svg>
<div class="thumbs">
  <div class="thumb" role="img" aria-label="Lounge with teal sofa" style="background:linear-gradient(#e8e6e0,#c9c6bc)"></div>
  <div class="thumb" role="img" aria-label="Bright bedroom" style="background:linear-gradient(#f0efea,#b8ab98)"></div>
  <div class="thumb" role="img" aria-label="Bedroom with wood floor" style="background:linear-gradient(#a8a498,#6a4e34)"></div>
  <div class="thumb" role="img" aria-label="Bed with colourful cushions" style="background:linear-gradient(#a86a3a,#e0d8cc)"></div>
  <div class="thumb" role="img" aria-label="Wood-panelled room" style="background:linear-gradient(#8c5c38,#d8d0c4)"></div>
  <div class="thumb" role="img" aria-label="Bed with colourful cushions" style="background:linear-gradient(#b07a3e,#e4dcd0)"></div>
  <div class="thumb" role="img" aria-label="Bedroom with wood floor" style="background:linear-gradient(#9ea09a,#6a4e34)"></div>
  <div class="thumb" role="img" aria-label="Bright bedroom" style="background:linear-gradient(#f0efea,#b8ab98)"></div>
</div>
<svg class="arrow" style="left:1070px" width="14" height="22" viewBox="0 0 14 22"><path d="M3 2l8 9-8 9" fill="none" stroke="var(--arrow)" stroke-width="3"/></svg>
<section class="welcome">
  <h1>Welcome to Corwith Lodge</h1>
  <p>Located in the heart of downtown Aspen, the newly renovated Corwith Lodge possesses all the charms of a vintage European Ski Lodge, while offering all of the modern conveniences one would expect with a stay in Aspen.A stay at our lodge includes free continental breakfast in our dining room, daily maid service, free wireless internet access, and a fully-equipped conference facility. Guests are also invited to relax in one of our two outdoor Jacuzzis or in our lounge, where a 42-inch plasma TV and fire-place make for a pleasant area to unwind.</p>
</section>
<footer class="footer">
  <a href="#">Home</a>| <a href="#">About</a> | <a href="#">Rooms</a>| <a href="#">Amenities</a>| <a href="#">Contact Us</a>
  <p>©2012 Corwith Lodge, Inc</p>
</footer>
</body>
</html>
```